House flipping business web site needed

birchstoneholdings.example.
I am a residential developer in Northern NJ and I am looking for a fresh new updated website. I have an intro video about my company being made now. I don't update it very often but I want an easy format that I can add update photos to on projects I have worked on or homes I renovate for sale.

Target Market(s)

investors into my projects so a portfolio , people looking to sell their homes to me.

Industry/Entity Type

Real Estate Development

Number of Pages Required

4 page

Font styles to use
Serif

Colors
33b8a4
39a9d7
cadf82

Requirements
Must have
• space for an intro video about my company
• a portfolio with pictures and information about each project
• Markets we serve- Morris County, NJ
• My logo- already created
• SEO
• Yes I would like this to function over all platforms. Phone, computer, all platforms.
• history and background page
• I am looking for a completed page that I can upload to the site that hosts my website
Nice to have
• I want something creative, easy to navigate. modern.

```html
<!DOCTYPE html>
<html lang="en">
<head>
<meta charset="utf-8">
<title>Birchstone Holdings</title>
<link href="https://fonts.googleapis.com/css2?family=Raleway:wght@400;500;600&family=Open+Sans:wght@400;600;700&family=Parisienne&display=swap" rel="stylesheet">
<style>
:root{
  --blue:#2fa4dc;
  --blue-deep:#2a8fbf;
  --teal-band:#3a9dbd;
  --ink:#555555;
  --ink-soft:#666666;
  --gray-bg:#ebebeb;
  --field-line:#cfcfcf;
  --footer:#555459;
  --white:#ffffff;
}
*{box-sizing:border-box;margin:0;padding:0}
html,body{width:1200px;height:2612px;overflow:hidden;background:var(--white)}
body{position:relative;font-family:"Open Sans",Arial,sans-serif;color:var(--ink)}
.abs{position:absolute}
.heading{font-family:"Raleway",Arial,sans-serif;font-weight:400;text-transform:uppercase;color:var(--ink)}
.heading .accent{color:var(--blue)}

/* top bar */
.topbar{left:0;top:0;width:1200px;height:40px;background:var(--blue)}
.topbar .contact{top:8px;color:var(--white);font-size:16px;display:flex;align-items:center;gap:10px}
.topbar .email{left:685px}
.topbar .phone{left:963px;font-weight:700;font-size:20px;top:5px}

/* header */
.header-wave{left:0;top:0;width:1200px;height:230px}
.brand{left:78px;top:80px;display:flex;align-items:center;gap:12px;font-family:"Raleway",Arial,sans-serif;font-weight:600;font-size:30px;color:var(--blue-deep);text-transform:uppercase;letter-spacing:1px}
.brand .dot{width:26px;height:26px;border-radius:50%;background:var(--blue-deep)}
.nav a{position:absolute;top:94px;font-family:"Raleway",Arial,sans-serif;font-size:23px;color:#444;text-decoration:none;text-transform:uppercase}
.nav a.active{color:var(--blue)}

/* hero */
.hero{left:0;top:150px;width:1200px;height:512px;background:linear-gradient(180deg,#3d5a2c 0%,#7f8a6a 45%,#8c8778 60%,#5e8a3a 85%,#4f7a30 100%)}
.tagline{left:0;top:662px;width:1200px;height:122px;background:linear-gradient(90deg,#2e8fb0,#45a9c6 50%,#2e8fb0);display:flex;align-items:center;justify-content:center;font-family:"Parisienne",cursive;font-size:46px;color:var(--white)}

/* portfolio */
.portfolio-title{left:0;top:832px;width:1200px;text-align:center;font-size:40px}
.portfolio-rule{left:522px;top:886px;width:157px;height:3px;background:var(--blue)}
.card{top:932px;width:235px;height:296px;background:var(--blue);color:var(--white);text-align:center;overflow:hidden}
.card .photo{position:absolute;left:0;top:0;width:235px;height:150px}
.card .wave{position:absolute;left:0;top:118px;width:235px;height:40px}
.card .title{position:absolute;left:0;top:162px;width:100%;font-family:"Raleway",Arial,sans-serif;font-size:21px;text-transform:uppercase}
.card .text{position:absolute;left:12px;top:196px;width:211px;font-size:15px;line-height:25px}
.card .more{position:absolute;left:0;top:252px;width:100%;font-size:17px;text-transform:uppercase}

/* welcome / quote */
.band{left:0;top:1292px;width:1200px;height:479px;background:var(--gray-bg)}
.welcome-kicker{left:80px;top:1342px;font-size:20px}
.welcome-title{left:78px;top:1378px;font-size:41px;color:var(--blue)}
.welcome-text{left:80px;top:1440px;width:505px;font-size:15.5px;line-height:25.5px;color:var(--ink-soft)}
.btn{background:var(--blue);color:var(--white);font-family:"Raleway",Arial,sans-serif;font-size:22px;text-transform:uppercase;display:flex;align-items:center;justify-content:center}
.quote-title{left:621px;top:1340px;font-size:41px}
.field{background:var(--white);border:1px solid var(--field-line);font-size:15px;color:#666;padding:10px 8px}

/* testimonial / news */
.section-title{top:1820px;font-size:41px}
.bubble{left:77px;top:1890px;width:491px;height:148px;background:var(--gray-bg);border-radius:8px}
.bubble-tail{left:228px;top:2036px;width:0;height:0;border-left:14px solid transparent;border-right:14px solid transparent;border-top:16px solid var(--gray-bg)}
.bubble .quote-mark{position:absolute;left:14px;top:14px;width:24px;height:22px}
.bubble p{position:absolute;left:40px;top:28px;width:430px;font-size:15.5px;line-height:25px;color:var(--ink-soft)}
.avatar{left:105px;top:2003px;width:104px;height:104px;border-radius:50%;border:4px solid var(--white);background:linear-gradient(180deg,#c9ccd1,#9aa3ad)}
.client-name{left:218px;top:2058px;font-family:"Raleway",Arial,sans-serif;font-size:21px;color:var(--blue)}
.arrow-btn{top:2128px;width:47px;height:49px;background:var(--blue)}
.news-item{left:621px;width:500px}
.news-item .ttl{font-size:19px;color:var(--blue)}
.news-item .date{font-size:14px;color:#888;margin-top:4px;display:flex;align-items:center;gap:7px}
.news-item .body{font-size:15.5px;line-height:25px;color:var(--ink-soft);margin-top:2px}
.news-rule{left:621px;top:1995px;width:502px;height:2px;background:#dcdcdc}

/* footer */
.footer-wave{left:0;top:2230px;width:1200px;height:60px}
.footer{left:0;top:2276px;width:1200px;height:284px;background:var(--footer)}
.footer-brand{left:101px;top:2412px;font-family:"Raleway",Arial,sans-serif;font-weight:600;font-size:27px;color:var(--white);text-transform:uppercase;letter-spacing:1px;display:flex;align-items:center;gap:10px;width:240px;line-height:32px}
.footer-brand .dot{flex:none;width:22px;height:22px;border-radius:50%;background:var(--blue)}
.footer-head{top:2338px;font-family:"Raleway",Arial,sans-serif;font-size:22px;color:var(--white);text-transform:uppercase}
.footer-links{left:350px;top:2378px;list-style:none}
.footer-links li{font-size:17px;line-height:37px;color:#d7d7d7}
.footer-links li:first-child{color:var(--white)}
.touch{left:608px;font-size:15.5px;color:var(--white);display:flex;gap:12px;line-height:24px}
.touch svg{flex:none;margin-top:4px}
.newsletter-text{left:890px;top:2378px;width:240px;font-size:15.5px;line-height:25px;color:var(--white)}
.copyright{left:0;top:2560px;width:1200px;height:52px;background:var(--blue);color:var(--white);font-size:15.5px;display:flex;align-items:center;justify-content:center}
</style>
</head>
<body>

<!-- hero photo -->
<div class="abs hero" role="img" aria-label="Photo of a weathered single-storey house with a shingle roof among tall green trees"></div>

<!-- header with wavy lower edge -->
<svg class="abs header-wave" viewBox="0 0 1200 230" preserveAspectRatio="none" aria-hidden="true">
  <path d="M0 0 H1200 V155 C960 130 760 150 560 190 C360 225 160 225 0 165 Z" fill="#ffffff"/>
  <path d="M0 165 C160 225 360 225 560 190 C760 150 960 130 1200 155" fill="none" stroke="#2fa4dc" stroke-width="9"/>
</svg>

<div class="abs topbar"></div>
<div class="abs topbar contact email">
  <svg width="20" height="15" viewBox="0 0 20 15"><rect x="1" y="1" width="18" height="13" fill="none" stroke="#fff" stroke-width="1.8"/><path d="M1 1 L10 8 L19 1" fill="none" stroke="#fff" stroke-width="1.8"/></svg>
  info@birchstoneholdings.example
</div>
<div class="abs topbar contact phone">
  <svg width="20" height="20" viewBox="0 0 24 24"><path d="M6.6 10.8a15 15 0 0 0 6.6 6.6l2.2-2.2a1 1 0 0 1 1-.25 11.4 11.4 0 0 0 3.6.6 1 1 0 0 1 1 1V20a1 1 0 0 1-1 1A17 17 0 0 1 3 4a1 1 0 0 1 1-1h3.5a1 1 0 0 1 1 1c0 1.25.2 2.45.6 3.6a1 1 0 0 1-.25 1z" fill="#fff"/></svg>
  123 456 7890
</div>

<div class="abs brand"><span class="dot"></span>Birchstone<br>Holdings</div>

<nav class="nav">
  <a class="active" style="left:547px">Home</a>
  <a style="left:675px">About</a>
  <a style="left:815px">Portfolio</a>
  <a style="left:1008px">Contact</a>
</nav>

<div class="abs tagline">We bring excellence to the home buying and renovation business.</div>

<!-- recent portfolio -->
<h2 class="abs heading portfolio-title">Recent <span class="accent">Portfolio</span></h2>
<div class="abs portfolio-rule"></div>

<div class="abs card" style="left:77px">
  <div class="photo" role="img" aria-label="Photo of a renovated grey two-storey house with trees" style="background:linear-gradient(180deg,#8fa3b8,#6e7f6a)"></div>
  <svg class="wave" viewBox="0 0 235 40" preserveAspectRatio="none"><path d="M0 14 C60 -4 140 34 235 8 V40 H0 Z" fill="#ffffff"/><path d="M0 22 C60 4 140 42 235 16 V40 H0 Z" fill="#2fa4dc"/></svg>
  <div class="title">Title</div>
  <div class="text">Lorem Ipsum is simply dummy text of the printing...</div>
  <div class="more">Read More &raquo;</div>
</div>
<div class="abs card" style="left:347px">
  <div class="photo" role="img" aria-label="Photo of a house frame under construction with wood sheathing" style="background:linear-gradient(180deg,#c7d2da,#8a6a4a)"></div>
  <svg class="wave" viewBox="0 0 235 40" preserveAspectRatio="none"><path d="M0 14 C60 -4 140 34 235 8 V40 H0 Z" fill="#ffffff"/><path d="M0 22 C60 4 140 42 235 16 V40 H0 Z" fill="#2fa4dc"/></svg>
  <div class="title">Title</div>
  <div class="text">Lorem Ipsum is simply dummy text of the printing...</div>
  <div class="more">Read More &raquo;</div>
</div>
<div class="abs card" style="left:618px">
  <div class="photo" role="img" aria-label="Photo of a renovated living room and kitchen with dark floors" style="background:linear-gradient(180deg,#d9d6cf,#3e3430)"></div>
  <svg class="wave" viewBox="0 0 235 40" preserveAspectRatio="none"><path d="M0 14 C60 -4 140 34 235 8 V40 H0 Z" fill="#ffffff"/><path d="M0 22 C60 4 140 42 235 16 V40 H0 Z" fill="#2fa4dc"/></svg>
  <div class="title">Title</div>
  <div class="text">Lorem Ipsum is simply dummy text of the printing...</div>
  <div class="more">Read More &raquo;</div>
</div>
<div class="abs card" style="left:888px">
  <div class="photo" role="img" aria-label="Photo of a stone chimney and yard in snow at dusk" style="background:linear-gradient(180deg,#7b90b5,#c9a98f 55%,#e7ecf2)"></div>
  <svg class="wave" viewBox="0 0 235 40" preserveAspectRatio="none"><path d="M0 14 C60 -4 140 34 235 8 V40 H0 Z" fill="#ffffff"/><path d="M0 22 C60 4 140 42 235 16 V40 H0 Z" fill="#2fa4dc"/></svg>
  <div class="title">Title</div>
  <div class="text">Lorem Ipsum is simply dummy text of the printing...</div>
  <div class="more">Read More &raquo;</div>
</div>

<!-- welcome and quote -->
<div class="abs band"></div>
<div class="abs heading welcome-kicker">Welcome to</div>
<h2 class="abs heading welcome-title">Birchstone Holdings</h2>
<p class="abs welcome-text">We are a team of experienced home buyers and renovators in the Morris County, NJ area. Our specialty is purchasing distressed homes and property. We then collaborate with the best talents in Northern New Jersey to renovate those properties and transform them into the best house in the neighborhood. As a result we create equity, a return on investment and most importantly we give home buyers a worry free property that provides a better way of life and hope for their future.</p>
<div class="abs btn" style="left:77px;top:1650px;width:172px;height:52px">Read More</div>

<h2 class="abs heading quote-title">Get a <span class="accent">Free Quote</span></h2>
<div class="abs field" style="left:618px;top:1411px;width:241px;height:40px">Enter Name</div>
<div class="abs field" style="left:880px;top:1411px;width:238px;height:40px">Enter Contact No.</div>
<div class="abs field" style="left:618px;top:1472px;width:500px;height:42px">Enter Email</div>
<div class="abs field" style="left:618px;top:1535px;width:500px;height:93px">Enter Contact No.</div>
<div class="abs btn" style="left:618px;top:1650px;width:147px;height:52px">Submit</div>

<!-- testimonial -->
<h2 class="abs heading section-title" style="left:79px">Client <span class="accent">Testimonial</span></h2>
<div class="abs bubble">
  <svg class="quote-mark" viewBox="0 0 24 22"><path d="M0 22V12C0 5 3 1 10 0v4C6 5 5 8 5 11h5v11zM14 22V12c0-7 3-11 10-12v4c-4 1-5 4-5 7h5v11z" fill="#2fa4dc"/></svg>
  <p>Lorem Ipsum is simply dummy text of the printing and typesetting industry. Lorem Ipsum has been the industry's standard dummy text ever since the 1500.</p>
</div>
<div class="abs bubble-tail"></div>
<div class="abs avatar" role="img" aria-label="Portrait photo of the client"></div>
<div class="abs client-name">Client Name</div>
<div class="abs arrow-btn" style="left:77px"><svg width="47" height="49" viewBox="0 0 47 49"><path d="M27 16 L19 24.5 L27 33" fill="none" stroke="#fff" stroke-width="2.5"/></svg></div>
<div class="abs arrow-btn" style="left:139px"><svg width="47" height="49" viewBox="0 0 47 49"><path d="M20 16 L28 24.5 L20 33" fill="none" stroke="#fff" stroke-width="2.5"/></svg></div>

<!-- news -->
<h2 class="abs heading section-title" style="left:621px">Latest <span class="accent">News</span></h2>
<div class="abs news-item" style="top:1884px">
  <div class="ttl">Lorem Ipsum is simply dummy text of the printing.</div>
  <div class="date"><svg width="13" height="13" viewBox="0 0 13 13"><rect x="0.5" y="2" width="12" height="10.5" fill="#999"/><rect x="2" y="5" width="9" height="6" fill="#fff"/></svg>18 October 2016</div>
  <div class="body">Lorem Ipsum is simply dummy text of the printing and typesetting industry. Lorem Ipsum has been the industry.</div>
</div>
<div class="abs news-rule"></div>
<div class="abs news-item" style="top:2009px">
  <div class="ttl">Lorem Ipsum is simply dummy text of the printing.</div>
  <div class="date"><svg width="13" height="13" viewBox="0 0 13 13"><rect x="0.5" y="2" width="12" height="10.5" fill="#999"/><rect x="2" y="5" width="9" height="6" fill="#fff"/></svg>18 October 2016</div>
  <div class="body">Lorem Ipsum is simply dummy text of the printing and typesetting industry. Lorem Ipsum has been the industry.</div>
</div>
<div class="abs btn" style="left:618px;top:2127px;width:147px;height:50px">View All</div>

<!-- footer -->
<div class="abs footer"></div>
<svg class="abs footer-wave" viewBox="0 0 1200 60" preserveAspectRatio="none" aria-hidden="true">
  <path d="M0 30 C250 60 450 60 700 40 C900 22 1050 4 1200 12 V60 H0 Z" fill="#555459"/>
  <path d="M0 30 C250 60 450 60 700 40 C900 22 1050 4 1200 12" fill="none" stroke="#2fa4dc" stroke-width="8"/>
</svg>

<div class="abs footer-brand"><span class="dot"></span><span>Birchstone Holdings</span></div>

<div class="abs footer-head" style="left:350px">Useful Links</div>
<ul class="abs footer-links">
  <li>Home</li><li>About</li><li>Portfolio</li><li>Services</li>
</ul>

<div class="abs footer-head" style="left:608px">Keep in Touch</div>
<div class="abs touch" style="top:2380px">
  <svg width="14" height="19" viewBox="0 0 14 19"><path d="M7 0a7 7 0 0 0-7 7c0 5 7 12 7 12s7-7 7-12a7 7 0 0 0-7-7zm0 9.5A2.5 2.5 0 1 1 7 4.5a2.5 2.5 0 0 1 0 5z" fill="#fff"/></svg>
  <span>Morris County, NJ |<br>973-555-0148</span>
</div>
<div class="abs touch" style="top:2440px">
  <svg width="17" height="17" viewBox="0 0 24 24"><path d="M6.6 10.8a15 15 0 0 0 6.6 6.6l2.2-2.2a1 1 0 0 1 1-.25 11.4 11.4 0 0 0 3.6.6 1 1 0 0 1 1 1V20a1 1 0 0 1-1 1A17 17 0 0 1 3 4a1 1 0 0 1 1-1h3.5a1 1 0 0 1 1 1c0 1.25.2 2.45.6 3.6a1 1 0 0 1-.25 1z" fill="#fff"/></svg>
  <span>123 456 7890</span>
</div>
<div class="abs touch" style="top:2482px">
  <svg width="18" height="14" viewBox="0 0 20 15"><rect x="1" y="1" width="18" height="13" fill="none" stroke="#fff" stroke-width="1.8"/><path d="M1 1 L10 8 L19 1" fill="none" stroke="#fff" stroke-width="1.8"/></svg>
  <span>info@birchstoneholdings.example</span>
</div>

<div class="abs footer-head" style="left:890px">Newsletter</div>
<p class="abs newsletter-text">Subscribe to stay on Birchstone Holdings</p>
<div class="abs field" style="left:890px;top:2432px;width:234px;height:35px;padding:7px 6px;border:none">Enter Email id</div>
<div class="abs btn" style="left:888px;top:2479px;width:162px;height:40px;font-size:20px">Subscribe</div>

<div class="abs copyright">&copy;&nbsp;<strong>Birchstone Holdings</strong>&nbsp;- 2016. All Rights Reserved.</div>

</body>
</html>
```